SilverLedgerOak - Double Sided Business Card

We are looking for design options or our business cards. We are a Business Solutions and HR solutions Provider - the theme is business, for this card.

Our brand colours are represented within our logo.

Details needed to be put on the front of the business card are:

Employees name: [Sample Name]
Role: [Sample Role]

Address: Suite 4 - Level 3/48 Halloran Avenue Parramatta NSW 2150
M: 0000 000 000
P: 1300 847 213
F: 1300 847 286
E: sample@silverledgeroak.com.au
www.silverledgeroak.com.au
Updates

Reason: Hello, could we please increase our deadline by 5 days. Thanking you, Tess

Target Market(s)

Business Owners, also Candidates looking for Employment

Industry/Entity Type

Business

Contact Information for Business Card

Role: [Sample Role]

M: 0000 000 000
P: 1300 847 213
F: 1300 847 286

Font styles to use
Sans Serif

Colors
3276b5
3176b5
0455a3
85abd2
cfdeed
ffffff
000000
1b1b1b
757575

Requirements
Must have
• Details needed to be put on the front of the business card are:
• Employees name: [Sample Name]
• Role: [Sample Role]
• Address: Suite 4 - Level 3/48 Halloran Avenue Parramatta NSW 2150
• M: 0000 000 000
• P: 1300 847 213
• F: 1300 847 286
• E: sample@silverledgeroak.com.au
• www.silverledgeroak.com.au
Nice to have
• Simplicity, clean and professional.

```html
<!DOCTYPE html>
<html lang="en">
<head>
<meta charset="utf-8">
<title>SilverLedgerOak Business Card</title>
<link href="https://fonts.googleapis.com/css2?family=Bebas+Neue&family=Questrial&display=swap" rel="stylesheet">
<style>
  :root {
    --brand-blue: #0455a3;
    --brand-navy: #13294b;
    --mid-blue: #3176b5;
    --ink: #1b1b1b;
    --paper: #ffffff;
    --card-edge: #757575;
  }
  * { margin: 0; padding: 0; box-sizing: border-box; }
  html, body {
    width: 1200px; height: 1200px; overflow: hidden;
    background: var(--paper);
  }
  .canvas { position: relative; width: 1200px; height: 1200px; }

  .card {
    position: absolute; left: 196px; width: 808px; height: 462px;
    overflow: hidden;
  }
  .card--front { top: 107px; border: 1px solid var(--card-edge); background: var(--paper); }
  .card--back {
    top: 600px;
    background:
      linear-gradient(135deg, var(--brand-navy) 0%, var(--brand-blue) 45%, var(--paper) 50%, var(--brand-blue) 55%, var(--brand-navy) 100%);
  }

  .front-content {
    position: absolute; width: 462px; height: 808px;
    left: 173px; top: -173px;
    transform: rotate(-90deg);
    font-family: "Questrial", sans-serif;
    color: var(--ink);
  }
  .line {
    position: absolute; left: 0; width: 100%;
    text-align: center; white-space: nowrap;
    transform: translateY(-50%);
  }
  .name {
    top: 202px; font-family: "Bebas Neue", sans-serif;
    font-size: 44px; letter-spacing: 3px; color: var(--brand-blue);
  }
  .role { top: 250px; font-size: 19px; letter-spacing: 3.4px; }
  .detail { font-size: 15.5px; letter-spacing: 1.1px; }
  .address-1 { top: 287px; }
  .address-2 { top: 316px; }
  .mobile { top: 345px; }
  .phone { top: 374px; }
  .fax { top: 402px; }
  .email { top: 433px; }
  .web { top: 465px; }

  .divider {
    position: absolute; top: 517px; left: 170px;
    width: 123px; height: 3px; background: var(--brand-blue);
  }

  .brand {
    position: absolute; top: 764px; left: 0; width: 100%;
    transform: translateY(-50%);
    display: flex; align-items: center; justify-content: center; gap: 10px;
    font-family: "Questrial", sans-serif; font-size: 25px;
    color: var(--brand-blue); letter-spacing: 0.5px;
  }
  .brand-square { width: 22px; height: 22px; background: var(--brand-blue); }
</style>
</head>
<body>
<main class="canvas">
  <section class="card card--front">
    <div class="front-content">
      <p class="line name">LIAM CARTER</p>
      <p class="line role">administrative assistant</p>
      <p class="line detail address-1">Suite 4 - Level 3/48 Halloran Avenue</p>
      <p class="line detail address-2">Parramatta, NSW 2150</p>
      <p class="line detail mobile">[m] 0000 000 000</p>
      <p class="line detail phone">[p] 1300 847 213</p>
      <p class="line detail fax">[f] 1300 847 286</p>
      <p class="line detail email">liam@silverledgeroak.com.au</p>
      <p class="line detail web">www.silverledgeroak.com.au</p>
      <div class="divider"></div>
      <div class="brand"><span class="brand-square"></span><span>SilverLedgerOak</span></div>
    </div>
  </section>
  <section class="card card--back" role="img" aria-label="Repeating brand cube pattern in navy and blue on white"></section>
</main>
</body>
</html>
```